" Temos como objetivo melhor atender as demandas atuais em TI com suporte de fácil acesso e analistas especializados com certificações que o mercado atual exige. Nossa equipe se dedica à prevenção, resolução de problemas e sugestões de melhorias do ambiente para garantir que seus servidores e aplicações estejam sempre no ar e funcionando, garantindo a continuidade dos negócios, foco das nossas soluções. "

```html
<!DOCTYPE html>
<html lang="pt-BR">
<head>
<meta charset="UTF-8">
<title>NOVARE – Crachá</title>
<link href="https://fonts.googleapis.com/css2?family=Montserrat:wght@400;500;600;700&display=swap" rel="stylesheet">
<style>
  :root{
    --navy:#111b2e;
    --navy-soft:#1a2640;
    --orange:#f0a229;
    --orange-deep:#e07b12;
    --white:#ffffff;
    --ink:#2a3142;
    --muted:#5a6072;
    --backdrop:#e4e5e7;
    --photo-a:#c9d3dc;
    --photo-b:#8d9aa8;
  }
  *{box-sizing:border-box;margin:0;padding:0}
  html,body{width:1200px;height:1200px;overflow:hidden}
  body{background:var(--backdrop);font-family:"Montserrat",sans-serif;position:relative}
  .badge{position:absolute;top:210px;width:456px;height:780px;border-radius:22px;overflow:hidden;box-shadow:0 10px 30px rgba(0,0,0,.12)}
  .badge--front{left:124px;background:var(--navy)}
  .badge--back{left:620px;background:var(--white)}
  .badge__slot{position:absolute;top:22px;left:50%;width:120px;height:18px;margin-left:-60px;border-radius:9px;background:var(--backdrop)}
  .badge__strip{position:absolute;left:0;right:0;bottom:0;height:14px;background:linear-gradient(90deg,var(--orange-deep),var(--orange))}
  .brand{position:absolute;top:168px;left:0;right:0;display:flex;justify-content:center;align-items:center;gap:14px}
  .brand__dot{width:38px;height:38px;border-radius:50%;background:var(--orange)}
  .brand__name{font-weight:500;font-size:40px;letter-spacing:8px}
  .badge--front .brand__name{color:var(--white)}
  .badge--back .brand__name{color:var(--navy)}
  .photo{position:absolute;top:283px;left:72px;width:312px;height:305px;border-radius:14px;background:linear-gradient(160deg,var(--photo-a),var(--photo-b))}
  .holder{position:absolute;top:632px;left:0;right:0;text-align:center}
  .holder__name{color:var(--orange);font-weight:600;font-size:29px;letter-spacing:.5px}
  .holder__role{color:var(--white);font-weight:400;font-size:22px;margin-top:4px}
  .field{position:absolute;left:32px;right:32px}
  .field__label{color:var(--orange);font-weight:600;font-size:17px;margin-bottom:10px}
  .field__box{height:56px;border:2px solid var(--ink);border-radius:12px}
  .field--name{top:278px}
  .field--id{top:388px}
  .field--dept{top:510px}
  .contacts{position:absolute;top:686px;left:32px;right:24px;display:grid;grid-template-columns:1fr 1fr;row-gap:12px;column-gap:10px}
  .contact{display:flex;align-items:center;gap:8px;color:var(--muted);font-size:12.5px;line-height:1.2}
  .contact__icon{flex:none;width:20px;height:20px;border-radius:50%;background:var(--orange);display:flex;align-items:center;justify-content:center}
</style>
</head>
<body>
  <section class="badge badge--front">
    <div class="badge__slot"></div>
    <div class="brand"><span class="brand__dot"></span><span class="brand__name">NOVARE</span></div>
    <div class="photo" role="img" aria-label="Foto do colaborador"></div>
    <div class="holder">
      <p class="holder__name">NOME E SOBRENOME</p>
      <p class="holder__role">Cargo | Função</p>
    </div>
    <div class="badge__strip"></div>
  </section>

  <section class="badge badge--back">
    <div class="badge__slot"></div>
    <div class="brand"><span class="brand__dot"></span><span class="brand__name">NOVARE</span></div>

    <div class="field field--name"><p class="field__label">Nome:</p><div class="field__box"></div></div>
    <div class="field field--id"><p class="field__label">RG:</p><div class="field__box"></div></div>
    <div class="field field--dept"><p class="field__label">DEPARTAMENTO:</p><div class="field__box"></div></div>

    <div class="contacts">
      <div class="contact">
        <span class="contact__icon"><svg width="11" height="11" viewBox="0 0 24 24"><path fill="#fff" d="M6.6 10.8a15 15 0 006.6 6.6l2.2-2.2c.3-.3.7-.4 1-.2 1.1.4 2.3.6 3.6.6.6 0 1 .4 1 1V20c0 .6-.4 1-1 1A17 17 0 013 4c0-.6.4-1 1-1h3.5c.6 0 1 .4 1 1 0 1.3.2 2.5.6 3.6.1.3 0 .7-.2 1z"/></svg></span>
        <span>(00) 0000-0000</span>
      </div>
      <div class="contact">
        <span class="contact__icon"><svg width="11" height="11" viewBox="0 0 24 24"><circle cx="12" cy="12" r="9" fill="none" stroke="#fff" stroke-width="2.2"/><path d="M3 12h18M12 3c3 3 3 15 0 18M12 3c-3 3-3 15 0 18" fill="none" stroke="#fff" stroke-width="2"/></svg></span>
        <span>www.exemplo.com.br</span>
      </div>
      <div class="contact">
        <span class="contact__icon"><svg width="11" height="11" viewBox="0 0 24 24"><rect x="3" y="5" width="18" height="14" rx="2" fill="#fff"/><path d="M3 6l9 7 9-7" fill="none" stroke="#f0a229" stroke-width="2"/></svg></span>
        <span>contato@exemplo.com</span>
      </div>
      <div class="contact">
        <span class="contact__icon"><svg width="11" height="11" viewBox="0 0 24 24"><path fill="#fff" d="M12 2a7 7 0 00-7 7c0 5 7 13 7 13s7-8 7-13a7 7 0 00-7-7zm0 9.5A2.5 2.5 0 1112 6.5a2.5 2.5 0 010 5z"/></svg></span>
        <span>rua exemplo, sl 000<br>cidade-UF, CEP: 00000-000</span>
      </div>
    </div>
    <div class="badge__strip"></div>
  </section>
</body>
</html>
```